Marcus Pellow Carpentry & Joinery

Hello, I would like a flyer designed for my new business doing small projects in my local area for home-owners. I am a professional tradesman.
The type of work I am offering is:
- decks/decking
- external stairs & railings
- install windows & doors
- roofs & gutters
- small additions
- built-in wardrobes
- finish work
- demolition

It would be great if the flyer could mention these, or use phrasing that fits this kind of construction work.
My idea for a slogan was "new work and repairs to any age home".

Please also mention FREE QUOTES and have my email and phone number included on the flyer, along with my carpentry licence number, which I can provided.

I'd like a one page, single-sided flyer that could be printed as DL.
Colour and style is up to you! I'll be placing this flyer on counters & in the windows of local businesses, so something simple and eye-catching is preferred.

Thank you!

```html
<!DOCTYPE html>
<html lang="en">
<head>
<meta charset="utf-8">
<title>Marcus Pellow Carpentry &amp; Joinery – Flyer</title>
<link rel="stylesheet" href="https://fonts.googleapis.com/css2?family=Alfa+Slab+One&family=Archivo+Black&family=Arvo:wght@700&display=swap">
<style>
  :root {
    --wood-light: #f0b85c;
    --wood-mid: #dd9434;
    --wood-dark: #c2741f;
    --brand-red: #6e0f0a;
    --brand-red-deep: #4a0805;
    --ink-white: #ffffff;
    --ink-black: #111111;
  }
  * { margin: 0; padding: 0; box-sizing: border-box; }
  html, body { width: 848px; height: 1200px; overflow: hidden; background: #ffffff; }
  .flyer {
    position: relative;
    width: 848px;
    height: 1200px;
    overflow: hidden;
  }
  .wood-backdrop {
    position: absolute;
    inset: 0;
    background: linear-gradient(90deg, var(--wood-dark) 0%, var(--wood-light) 22%, var(--wood-mid) 45%, var(--wood-light) 68%, var(--wood-dark) 100%);
  }
  .brand-name {
    position: absolute;
    left: 0; right: 0;
    top: 120px;
    text-align: center;
    font-family: "Arvo", Georgia, serif;
    font-weight: 700;
    color: var(--brand-red);
  }
  .brand-name .owner { display: block; font-size: 78px; line-height: 1.1; }
  .brand-name .trade { display: block; font-size: 46px; line-height: 1.3; margin-top: 18px; }
  .slogan {
    position: absolute;
    left: 0; right: 0;
    top: 478px;
    text-align: center;
    transform: rotate(-8deg);
    font-family: "Alfa Slab One", Georgia, serif;
    font-size: 80px;
    line-height: 1.06;
    color: var(--ink-white);
    text-shadow:
      3px 3px 0 var(--brand-red), -3px -3px 0 var(--brand-red),
      3px -3px 0 var(--brand-red), -3px 3px 0 var(--brand-red),
      0 4px 0 var(--brand-red), 0 -4px 0 var(--brand-red),
      4px 0 0 var(--brand-red), -4px 0 0 var(--brand-red),
      7px 9px 6px rgba(60, 20, 0, 0.6);
  }
  .free-quotes {
    position: absolute;
    left: 0; right: 0;
    top: 862px;
    text-align: center;
    font-family: "Alfa Slab One", Georgia, serif;
    font-size: 76px;
    letter-spacing: 3px;
    color: var(--brand-red);
    text-shadow: 2px 2px 0 var(--brand-red-deep);
  }
  .phone {
    position: absolute;
    left: 0; right: 0;
    top: 952px;
    text-align: center;
    font-family: "Archivo Black", Arial, sans-serif;
    font-size: 80px;
    letter-spacing: 2px;
    color: var(--ink-white);
    text-shadow:
      3px 3px 0 var(--brand-red-deep), -3px -3px 0 var(--brand-red-deep),
      3px -3px 0 var(--brand-red-deep), -3px 3px 0 var(--brand-red-deep),
      5px 6px 4px rgba(40, 10, 0, 0.55);
  }
  .email {
    position: absolute;
    left: 0; right: 0;
    top: 1052px;
    text-align: center;
    font-family: "Arvo", Georgia, serif;
    font-weight: 700;
    font-size: 34px;
    color: var(--brand-red);
    text-shadow: 1px 1px 0 rgba(255, 230, 190, 0.6);
  }
  .licence {
    position: absolute;
    left: 0; right: 0;
    top: 1116px;
    text-align: center;
    font-family: "Arvo", Georgia, serif;
    font-weight: 700;
    font-size: 26px;
    letter-spacing: 1px;
    color: var(--ink-black);
    text-shadow:
      2px 2px 0 var(--ink-white), -2px -2px 0 var(--ink-white),
      2px -2px 0 var(--ink-white), -2px 2px 0 var(--ink-white);
  }
</style>
</head>
<body>
  <main class="flyer">
    <div class="wood-backdrop" role="img" aria-label="Background of vertical warm timber planks with wood grain"></div>

    <h1 class="brand-name">
      <span class="owner">Marcus Pellow</span>
      <span class="trade">Carpentry &amp; Joinery</span>
    </h1>

    <p class="slogan">New work and<br>repairs to<br>any age home!</p>

    <p class="free-quotes">FREE QUOTES</p>
    <p class="phone">0400 555 218</p>
    <p class="email">marcuspellow15@inboxmail.com</p>
    <p class="licence">SBC Licence number: 4839205</p>
  </main>
</body>
</html>
```